Ridgemoor Partners

Need a new website - see more on ridgemoorpartners.com

Target Market(s)

Finance industry = conservative design

Coding

Coded - Design and coding required

Number of Pages Required

5+ page

Requirements
Should not have
• Dear all,
• Please avoid pictures of people on the website (except the "team" of course :-)

```html
<!DOCTYPE html>
<html lang="en">
<head>
<meta charset="utf-8">
<title>Ridgemoor Partners</title>
<link href="https://fonts.googleapis.com/css2?family=Roboto:wght@400;500;700&display=swap" rel="stylesheet">
<style>
:root{
  --red:#d0232a;
  --navy:#1f2b7a;
  --ink:#1d1d1f;
  --muted:#5f6266;
  --light:#f4f5f7;
  --rule:#dadce0;
  --white:#ffffff;
}
*{box-sizing:border-box;margin:0;padding:0}
html,body{width:1200px;height:3056px;overflow:hidden}
body{font-family:"Roboto",Arial,sans-serif;color:var(--ink);background:var(--white);position:relative}
a{color:inherit;text-decoration:none}

/* hero */
.hero{position:absolute;left:0;top:0;width:1200px;height:546px;
  background:
    radial-gradient(ellipse 420px 260px at 520px 330px,rgba(40,48,60,.55),rgba(40,48,60,0)),
    radial-gradient(ellipse 300px 280px at 1080px 360px,rgba(50,58,68,.6),rgba(50,58,68,0)),
    radial-gradient(ellipse 260px 240px at 200px 380px,rgba(110,70,50,.45),rgba(110,70,50,0)),
    linear-gradient(180deg,#6f7f96 0%,#9ba7b6 22%,#b4b8b8 40%,#6e6f70 58%,#4d4a46 78%,#3a3a3c 100%)}
.site-nav{position:absolute;left:0;top:0;width:1200px;height:68px;
  background:linear-gradient(180deg,rgba(0,0,0,.4),rgba(0,0,0,0));border-bottom:1px solid rgba(255,255,255,.25)}
.brand{position:absolute;left:57px;top:11px;display:flex;align-items:center;gap:12px;color:var(--white);font-weight:700;font-size:17px}
.brand-dot{width:46px;height:46px;border-radius:50%;background:var(--red)}
.main-menu{position:absolute;left:418px;top:24px;display:flex;gap:36px;color:var(--white);font-weight:700;font-size:15px}
.nav-actions{position:absolute;left:943px;top:17px;display:flex;gap:8px}
.pill{height:32px;padding:0 15px;border-radius:16px;border:1.5px solid var(--white);color:var(--white);font-size:14px;display:flex;align-items:center}
.pill.solid{background:var(--white);color:var(--ink)}

.sub-bar{position:absolute;left:0;top:546px;width:1200px;height:33px;background:var(--light);border-bottom:1px solid var(--rule);
  font-size:13px;color:var(--muted)}
.sub-links{position:absolute;left:51px;top:8px;display:flex;gap:20px}
.social{position:absolute;left:1005px;top:8px;display:flex;gap:27px;align-items:center}
.sq{width:16px;height:16px;border-radius:2px}

/* intro */
.intro{position:absolute;top:579px;left:0;width:1200px;height:165px;text-align:center}
.intro h1{font-weight:400;font-size:21px;line-height:29px;margin-top:14px}
.intro p{font-size:13px;color:var(--muted);margin-top:6px}
.outline-btn{display:inline-flex;align-items:center;gap:8px;height:38px;padding:0 20px;border:1.5px solid var(--red);border-radius:19px;font-size:14px;font-weight:500;color:var(--ink);margin-top:14px}

/* solutions */
.solutions{position:absolute;top:744px;left:0;width:1200px;height:580px;background:var(--light)}
.section-title{text-align:center;font-weight:700;font-size:24px}
.section-title span{color:var(--red)}
.dotted{width:1096px;margin:10px auto 0;border-top:2px dotted var(--red)}
.solutions .section-title{margin-top:22px}
.service{position:absolute;top:134px;width:340px;text-align:center}
.service .circle{position:relative;width:178px;height:178px;border-radius:50%;margin:0 auto;display:flex;align-items:center;justify-content:center}
.service .circle::after{content:"";position:absolute;inset:8px;border-radius:50%;border:1.5px solid rgba(255,255,255,.35)}
.service h3{font-size:17px;font-weight:700;margin-top:34px}
.service h3.accent{color:var(--red)}
.service p{font-size:13px;line-height:20px;color:var(--muted);margin-top:12px}
.service .outline-btn{margin-top:18px;font-size:13px;height:36px;padding:0 18px}
.service .outline-btn.dark{border-color:var(--ink)}

/* about */
.about-band{position:absolute;top:1623px;left:0;width:1200px;height:508px;
  background:radial-gradient(ellipse 500px 300px at 300px 120px,rgba(70,80,150,.45),rgba(70,80,150,0)),linear-gradient(180deg,#27348a,#1c2670)}
.team-photo{position:absolute;left:287px;top:1342px;width:628px;height:381px;
  background:
    radial-gradient(ellipse 140px 190px at 420px 230px,#2b2e35 0%,#3a3e46 60%,rgba(58,62,70,0) 100%),
    linear-gradient(90deg,#dfe4ea 0%,#c4ccd4 30%,#eef1f4 55%,#b8c0c8 80%,#8d96a0 100%)}
.about-text{position:absolute;top:1783px;left:0;width:1200px;color:var(--white)}
.about-text .kicker{text-align:center;font-size:16px}
.about-text h2{text-align:center;font-size:36px;font-weight:400;margin-top:4px}
.bios{display:flex;gap:36px;padding:0 51px;margin-top:20px}
.bio{flex:1}
.bio h3{text-align:center;font-size:17px;font-weight:700}
.bio p{font-size:11.6px;line-height:19px;text-align:center;margin-top:6px}

/* news */
.news{position:absolute;top:2131px;left:0;width:1200px;height:517px}
.news .section-title{margin-top:30px}
.cards{display:flex;gap:29px;padding:0 53px;margin-top:62px}
.card{width:252px;height:356px;background:var(--light)}
.card .thumb{height:191px}
.card h4{font-size:18px;font-weight:500;margin:18px 18px 0}
.card p{font-size:13px;line-height:19px;color:var(--muted);margin:10px 18px 0}
.card .meta{margin:18px 18px 0;border-top:1px solid var(--rule);padding-top:12px;display:flex;justify-content:space-between;font-size:11px;color:var(--muted)}

/* offices */
.offices{position:absolute;top:2648px;left:0;width:1200px;height:245px;background:var(--light)}
.office{position:absolute;top:42px;font-size:14px;line-height:22px}
.office h3{font-size:21px;font-weight:400;padding-bottom:10px;border-bottom:1px solid var(--rule);margin-bottom:18px}
.office h4{font-size:15px;font-weight:700}
.office.lux h3{border-bottom:2px solid var(--red)}
.office-cols{position:relative;height:70px}
.office-cols > div{position:absolute;top:0}

/* footer */
.site-footer{position:absolute;top:2893px;left:0;width:1200px;height:163px;border-top:3px solid var(--red);border-bottom:6px solid var(--red)}
.foot-menu{position:absolute;left:50px;top:46px;display:flex;gap:26px;align-items:center;font-size:13px;font-weight:700}
.foot-line{position:absolute;left:50px;right:50px;top:74px;border-top:1px solid var(--rule)}
.foot-links{position:absolute;left:53px;top:92px;display:flex;gap:20px;font-size:11px}
.foot-legal{position:absolute;right:50px;top:92px;display:flex;gap:20px;font-size:11px}
.foot-brand{position:absolute;right:50px;top:14px;display:flex;align-items:center;gap:10px;font-size:15px;font-weight:700;color:var(--red)}
.foot-brand .brand-dot{width:50px;height:50px}
</style>
</head>
<body>

<header class="hero" role="img" aria-label="City skyline of glass office towers under a cloudy sky">
  <nav class="site-nav">
    <a class="brand" href="#"><span class="brand-dot"></span>Ridgemoor Partners</a>
    <div class="main-menu"><a href="#">OUR SERVICES</a><a href="#">NEWS</a><a href="#">TEAM</a><a href="#">CONTACT</a></div>
    <div class="nav-actions"><a class="pill" href="#">Log In</a><a class="pill solid" href="#">Current Engagements</a></div>
  </nav>
</header>

<div class="sub-bar">
  <div class="sub-links"><span>Learn More:</span><a href="#">Our Company</a><a href="#">Careers</a><a href="#">Help &amp; Contact</a></div>
  <div class="social">
    <span class="sq" style="background:#3b5998"></span>
    <span class="sq" style="background:#1da1f2"></span>
    <span class="sq" style="background:#d34836"></span>
    <svg width="14" height="14" viewBox="0 0 14 14"><circle cx="6" cy="6" r="4.5" fill="none" stroke="#666" stroke-width="1.6"/><line x1="9.3" y1="9.3" x2="13" y2="13" stroke="#666" stroke-width="1.8"/></svg>
  </div>
</div>

<section class="intro">
  <h1>Founded in 2004, Ridgemoor is headquartered in Gibraltar<br>with representative offices in Luxembourg and London</h1>
  <p>See some of the features below and learn why businesses trust Ridgemoor</p>
  <a class="outline-btn" href="#"><svg width="10" height="12" viewBox="0 0 10 12"><path d="M0 0L10 6L0 12Z" fill="#d0232a"/></svg>Learn about Ridgemoor</a>
</section>

<section class="solutions">
  <h2 class="section-title">A solution <span>for your business</span></h2>
  <div class="dotted"></div>
  <div class="service" style="left:54px">
    <div class="circle" role="img" aria-label="Blue circular illustration of factory buildings" style="background:radial-gradient(circle at 40% 35%,#3a9bd0,#1a6c9e 55%,#0c4670)"></div>
    <h3>Mergers &amp; Acquisitions</h3>
    <p>Ridgemoor Partners efficiently arranges both equity and debt financing by offering new capital to public and private companies.</p>
    <a class="outline-btn" href="#">Learn More</a>
  </div>
  <div class="service" style="left:431px">
    <div class="circle" style="background:radial-gradient(circle at 40% 35%,#f6ae2a,#dc8a08 60%,#b46c00);border:4px solid #8a5000">
      <svg width="96" height="80" viewBox="0 0 96 80" aria-hidden="true">
        <g fill="none" stroke="#fff" stroke-width="4" stroke-linecap="round" stroke-linejoin="round">
          <path d="M6 20h18c14 0 22 40 36 40h24"/>
          <path d="M6 60h18c14 0 22-40 36-40h24"/>
          <path d="M74 10l12 10-12 10"/>
          <path d="M74 50l12 10-12 10"/>
        </g>
      </svg>
    </div>
    <h3 class="accent">Reverse Mergers &amp; Alternative Offerings</h3>
    <p>We advise in mergers &amp; acquisitions, roll-up strategies, joint ventures, recapitalizations, operate restructuring, and spin-offs.</p>
    <a class="outline-btn dark" href="#">More on Reverse &amp; Alternative</a>
  </div>
  <div class="service" style="left:804px">
    <div class="circle" role="img" aria-label="Teal circular illustration of business figures" style="background:radial-gradient(circle at 40% 35%,#2aa3ab,#12767e 55%,#0a4e55)"></div>
    <h3>Private Placements</h3>
    <p>Ridgemoor Partners assists fast growing privately-held companies with easy and affordable access to the public markets in the U.S.</p>
    <a class="outline-btn" href="#">Learn More</a>
  </div>
</section>

<section class="about-band"></section>
<div class="team-photo" role="img" aria-label="Portrait of the managing director in a bright office"></div>
<div class="about-text">
  <p class="kicker">Our Little Story</p>
  <h2>Something About Us</h2>
  <div class="bios">
    <div class="bio">
      <h3>Anders Holm, Managing Director</h3>
      <p>Mr. Holm, an international financier, has over 25 years experience in the global financial services industry as a securities professional. From 1996 through 2003, Mr. Holm was Co-Founder and Managing Partner of Meridian Capital in London, in charge of the private placement division of the company. Mr. Holm started his career in 1986 with Nordhavn Bank in Copenhagen, Denmark. In early 2004, Mr. Holm launched a new investment holding company, Ridgemoor Partners, serving as Managing Director and overseeing the company's overall investments, investment banking practice, including origination, structuring and financing of both privately-held and publicly traded emerging growth companies in North America, Asia and Europe.</p>
    </div>
    <div class="bio">
      <h3>Lars Vendel, Managing Partner</h3>
      <p>Mr. Vendel has an impressive resume as a stock broker and equity portfolio manager with a widespread aspect of highly acknowledged investment funds. After working within this segment of finance for roughly 13 years, he advanced into performing reverse mergers, PPMs and IPOs in the US, making him a strong profile within the transatlantic investment arena as well as an esteemed real estate investor. Since 2010, Mr. Vendel has served as a trusted introducer between highly acknowledged investment organizations and private high net worth individuals. Thus he brings an unprecedented network of both private and institutional investors to the Ridgemoor family.</p>
    </div>
  </div>
</div>

<section class="news">
  <h2 class="section-title">Latest <span>News &amp; Views</span></h2>
  <div class="dotted"></div>
  <div class="cards">
    <article class="card"><div class="thumb" role="img" aria-label="Traveller walking with a leather bag past a wooden wall" style="background:radial-gradient(ellipse 70px 110px at 90px 80px,#3c4a66,rgba(60,74,102,0)),linear-gradient(90deg,#e6e2dc 0%,#cfc6bb 40%,#7a4e2e 60%,#4a2e1c 100%)"></div>
      <h4>Standard Post</h4><p>Enim congue blandit. Lorem ipsum dolor sit amet, consectetur adipiscing elit. Quisque...</p>
      <div class="meta"><span>22 June, 2015</span><span>0</span></div></article>
    <article class="card"><div class="thumb" role="img" aria-label="Glass coffee carafe on a wooden table" style="background:radial-gradient(ellipse 50px 70px at 140px 110px,#4a3426,rgba(74,52,38,0)),linear-gradient(180deg,#f2f0ec 0%,#e4e0da 60%,#8a6a50 80%,#5a4030 100%)"></div>
      <h4>Video Post</h4><p>Ultrices posuere cubilia curae curabitur sit amet tortor ut massa commodo. Vestibulum...</p>
      <div class="meta"><span>22 June, 2015</span><span>0</span></div></article>
    <article class="card"><div class="thumb" role="img" aria-label="Cafe interior with brick wall, table and white chairs" style="background:radial-gradient(ellipse 60px 40px at 80px 150px,#f0eeea,rgba(240,238,234,0)),linear-gradient(180deg,#9a6a4a 0%,#b07a58 45%,#7a5238 70%,#c8b8a4 100%)"></div>
      <h4>Post with Image</h4><p>Enim congue blandit. Lorem ipsum dolor sit amet, consectetur adipiscing elit. Quisque...</p>
      <div class="meta"><span>22 June, 2015</span><span>0</span></div></article>
    <article class="card"><div class="thumb" role="img" aria-label="Leather wallet on a desk in front of a pinboard" style="background:radial-gradient(ellipse 90px 45px at 120px 130px,#6a3a22,rgba(106,58,34,0)),linear-gradient(180deg,#e8e2da 0%,#d6ccc0 55%,#bfb2a4 100%)"></div>
      <h4>Image Post</h4><p>Ultrices posuere cubilia curae curabitur sit amet tortor ut massa commodo. Vestibulum...</p>
      <div class="meta"><span>22 June, 2015</span><span>3</span></div></article>
  </div>
</section>

<section class="offices">
  <div class="office" style="left:28px;width:560px">
    <h3>Beverly Hills Offices</h3>
    <div class="office-cols">
      <div style="left:0"><h4>California</h4>210 Larchmont Drive - Suite 120<br>Beverly Hills, CA 90210</div>
      <div style="left:294px"><h4>Contact Info</h4>Phone: +1 310 555 0142<br>Email: info@ridgemoorpartners.com</div>
    </div>
  </div>
  <div class="office lux" style="left:615px;width:265px">
    <h3>Luxembourg Offices</h3>
    <h4>Luxembourg</h4>14, Rue des Tilleuls 2450<br>Luxembourg<br>Phone: +352 555 210 044
  </div>
  <div class="office" style="left:908px;width:264px">
    <h3>London Offices</h3>
    <h4>England</h4>22 Aldgate Row<br>EC3N 1AB London<br>Phone: +44 (0) 7700 900 412
  </div>
</section>

<footer class="site-footer">
  <div class="foot-menu">
    <svg width="14" height="14" viewBox="0 0 14 14"><circle cx="6" cy="6" r="4.5" fill="none" stroke="#666" stroke-width="1.6"/><line x1="9.3" y1="9.3" x2="13" y2="13" stroke="#666" stroke-width="1.8"/></svg>
    <a href="#">Help &amp; Contact</a><a href="#">Services</a><a href="#">News</a><a href="#">Current Engagements</a>
  </div>
  <div class="foot-brand"><span class="brand-dot"></span>Ridgemoor Partners</div>
  <div class="foot-line"></div>
  <div class="foot-links"><a href="#">About</a><a href="#">Team</a><a href="#">Careers</a><a href="#">Public Policy</a><a href="#">Sitemap</a><a href="#">People</a><a href="#">Partners</a></div>
  <div class="foot-legal"><span>© 2006 - 2018</span><a href="#">Privacy</a><a href="#">Legal</a><a href="#">Feedback</a></div>
</footer>

</body>
</html>
```